Infant Massage Instructor Business Card Design

I need a business card in order to advertise my private and group parent instruction classes for massaging their infants. I am in Boulder, Colorado. I most often teach people in their own homes, but will offer group classes in other public facility venues.
I would like to use peach and lavender/ purple colors, very soft, round but clearly legible font and design. I would love to have a simple, sweeping, soft line graphic of an infant (perhaps held in adult hands?) reaching towards my business name; "Tenderly Tended Infant Massage". "Power Points" are: Reading Infant Cues, Strengthening Parent Intuition, and Nurturing Family Bonds.
"Private and group classes offered, sliding scale rates available."
THE ATTACHED LOGO IS THE LOGO OF THE "GLOBAL SOCIETY FOR BABY TOUCH", my R.B.T.P. certifying agency.

"Properly" spelled, my first name has an accent exactly over the 'e'. The top of the accent leans to the right. I would like for the name of the business to appear foremost, over my own name (which is hard for people to pronounce and 'get'). Thank you for your care and creativity in helping me promote this beautiful service offering!

I will be considering a letterhead design and postcard / brochure design as well. Please keep that in mind as you design! Thank you!

Target Market(s)

New moms and dads. Young adults to 50. Single parents, adoptive parents. Mixed economic status.

Industry/Entity Type

Adult

Contact Information for Business Card

Tenderly Tended Infant Massage
Morvel Oskin, R.B.T.P.
303-555-0182

Colors
b868aa
e667a6
a64599
f68e4e
f9bb93
f37123

Requirements
Must have
• Soft, curvy, simple line drawing of infant.
Nice to have
• Infant image, being held in adult hands
Should not have
• No "cutesy" look, please! No cartoon-like images.

```html
<!DOCTYPE html>
<html lang="en">
<head>
<meta charset="utf-8">
<title>Tenderly Tended Infant Massage – Business Card</title>
<link href="https://fonts.googleapis.com/css2?family=Quicksand:wght@600&family=PT+Serif:ital@1&display=swap" rel="stylesheet">
<style>
  :root {
    --page: #ffffff;
    --peach: #f9e4d4;
    --lavender: #e6d8e8;
    --logo-purple: #a98bc6;
    --text-purple: #9a7fc0;
    --mark-peach: #f3b3a0;
  }
  html, body {
    margin: 0;
    width: 1200px;
    height: 1200px;
    overflow: hidden;
    background: var(--page);
  }
  .card {
    position: absolute;
    left: 274px;
    top: 388px;
    width: 727px;
    height: 415px;
    border-radius: 18px;
    overflow: hidden;
  }
  .card__top {
    position: absolute;
    left: 0; top: 0;
    width: 100%;
    height: 234px;
    background: var(--peach);
  }
  .card__bottom {
    position: absolute;
    left: 0; top: 234px;
    width: 100%;
    height: 181px;
    background: var(--lavender);
    text-align: center;
    font-family: "PT Serif", Georgia, serif;
    font-style: italic;
    color: var(--text-purple);
  }
  .brand-mark {
    position: absolute;
    left: 60px;
    top: 44px;
  }
  .brand {
    position: absolute;
    right: 74px;
    top: 32px;
    text-align: right;
    font-family: "Quicksand", Arial, sans-serif;
    font-weight: 600;
    color: var(--logo-purple);
    line-height: 1;
  }
  .brand__line1 { font-size: 45px; letter-spacing: 0.5px; }
  .brand__line2 { font-size: 38px; margin-top: 4px; letter-spacing: 1.5px; }
  .contact {
    position: absolute;
    right: 78px;
    top: 132px;
    text-align: right;
    font-family: "PT Serif", Georgia, serif;
    font-style: italic;
    color: var(--text-purple);
    line-height: 1.25;
  }
  .contact__name { font-size: 29px; }
  .contact__phone { font-size: 27px; }
  .tagline {
    margin: 20px 0 0;
    font-size: 26px;
    line-height: 33px;
  }
  .offer {
    margin: 11px 0 0;
    font-size: 19px;
  }
  .website {
    margin: 10px 0 0;
    font-size: 18px;
  }
</style>
</head>
<body>
  <div class="card">
    <div class="card__top">
      <svg class="brand-mark" width="60" height="60" viewBox="0 0 60 60" role="img" aria-label="Brand mark for Tenderly Tended Infant Massage">
        <circle cx="30" cy="30" r="30" fill="var(--mark-peach)"/>
      </svg>
      <div class="brand">
        <div class="brand__line1">tenderly tended</div>
        <div class="brand__line2">infant massage</div>
      </div>
      <div class="contact">
        <div class="contact__name">Morvel Oskin, R.B.T.P.</div>
        <div class="contact__phone">303-555-0182</div>
      </div>
    </div>
    <div class="card__bottom">
      <p class="tagline">Reading Infant Cues, Strengthening Parent<br>Intuition, and Nurturing Family Bonds.</p>
      <p class="offer">Private and group classes offered. Sliding scale rates available.</p>
      <p class="website">www.tenderlytendedinfantmassage.com</p>
    </div>
  </div>
</body>
</html>
```